Velmo BUSINESS CARD

Design an attention-grabbing business cards. Draw inspiration from the provided logo file. Please use the same font style as in the logo.
the back side of the card is for accent/decoration.

Contact Information for Business Card

PLEASE USE PROVIDED BUSINESS CARD SAMPLE

Other font styles liked:
• LUMETTE

Colors
EB3D1F
EC4F4E
F09395
F8D3D4
FCEDEE

Requirements
Must have
• RED, BLACK COLORS, SOLID BACK COLOR
Nice to have
• MAKE IT FANCY

```html
<!DOCTYPE html>
<html lang="en">
<head>
<meta charset="utf-8">
<title>Velmo Business Cards</title>
<link rel="stylesheet" href="https://fonts.googleapis.com/css2?family=Orbitron:wght@700;900&family=Mulish:ital,wght@0,400;0,700;1,400&display=swap">
<style>
  :root {
    --red: #de232f;
    --black: #231f20;
    --white: #ffffff;
    --page: #ffffff;
    --shadow: 0 6px 14px rgba(0,0,0,.22);
  }
  * { box-sizing: border-box; margin: 0; padding: 0; }
  html, body { width: 1200px; height: 662px; overflow: hidden; background: var(--page); }
  .canvas { position: relative; width: 1200px; height: 662px; }
  .card { position: absolute; width: 351px; height: 200px; background: var(--white); box-shadow: var(--shadow); overflow: hidden; }
  .card svg.bg { position: absolute; inset: 0; }
  .front-dark { left: 39px; top: 133px; z-index: 1; }
  .front-light { left: 806px; top: 133px; z-index: 1; }
  .back-white { left: 247px; top: 322px; z-index: 2; border: 1px solid #e6e6e6; }
  .back-red { left: 632px; top: 322px; z-index: 2; background: var(--red); }

  .holder-name { position: absolute; left: 21px; top: 22px; font-family: "Orbitron", sans-serif; font-weight: 700; font-size: 16px; letter-spacing: 1px; color: var(--white); white-space: nowrap; }
  .holder-role { position: absolute; left: 21px; top: 42px; font-family: "Mulish", sans-serif; font-style: italic; font-size: 9px; letter-spacing: 1px; color: var(--white); }

  .contact { position: absolute; display: flex; align-items: flex-start; gap: 7px; font-family: "Mulish", sans-serif; font-size: 9.5px; line-height: 11px; letter-spacing: .9px; color: var(--red); white-space: nowrap; }
  .contact svg { width: 10px; height: 10px; flex: none; margin-top: 1px; }
  .contact em { font-style: italic; }
  .contact.web { font-weight: 700; }
  .contact.web.on-red { color: var(--white); }

  .brand { position: absolute; left: 0; right: 0; top: 72px; display: flex; justify-content: center; align-items: center; gap: 14px; }
  .brand-square { width: 54px; height: 54px; background: var(--black); flex: none; }
  .brand-name { font-family: "Orbitron", sans-serif; font-weight: 900; font-size: 44px; line-height: 44px; letter-spacing: 3px; color: var(--black); }
</style>
</head>
<body>
<div class="canvas">

  <section class="card front-dark">
    <svg class="bg" width="351" height="200" viewBox="0 0 351 200">
      <path d="M0 0 H229 C205 38 160 64 82 66 H0 Z" fill="var(--black)"/>
      <circle cx="293" cy="95" r="95" fill="var(--red)" role="img" aria-label="Red dragon emblem illustration"/>
      <path d="M128 200 C150 172 188 160 236 160 H351 V200 Z" fill="var(--red)"/>
    </svg>
    <div class="holder-name">DANE ORWELL</div>
    <div class="holder-role">President</div>
    <div class="contact" style="left:22px;top:84px"><svg viewBox="0 0 10 10"><rect x="2.5" y=".5" width="5" height="9" rx="1" fill="none" stroke="var(--red)"/></svg><span><em>Office</em> 555-014-2290</span></div>
    <div class="contact" style="left:22px;top:106px"><svg viewBox="0 0 10 10"><rect x=".5" y="1.5" width="9" height="7" rx="1.5" fill="none" stroke="var(--red)"/><line x1="3.5" y1="1.5" x2="3.5" y2="8.5" stroke="var(--red)"/></svg><span><em>Cell</em> 555-018-3316</span></div>
    <div class="contact" style="left:22px;top:128px"><svg viewBox="0 0 10 10"><rect x=".5" y="2" width="9" height="6" fill="none" stroke="var(--red)"/><path d="M.5 2 L5 5.5 L9.5 2" fill="none" stroke="var(--red)"/></svg><span>DOrwell@velmo-llc.com</span></div>
    <div class="contact" style="left:22px;top:151px"><svg viewBox="0 0 10 10"><path d="M5 9.5 C2 6 1.5 4.5 1.5 3.5 a3.5 3.5 0 0 1 7 0 C8.5 4.5 8 6 5 9.5 Z" fill="none" stroke="var(--red)"/><circle cx="5" cy="3.6" r="1.2" fill="var(--red)"/></svg><span>1840 N. 200 East<br>Ashford, IN, 46000</span></div>
    <div class="contact web on-red" style="left:196px;top:163px"><svg viewBox="0 0 10 10"><circle cx="5" cy="5" r="4.5" fill="none" stroke="var(--white)"/><ellipse cx="5" cy="5" rx="2" ry="4.5" fill="none" stroke="var(--white)"/><line x1=".5" y1="5" x2="9.5" y2="5" stroke="var(--white)"/></svg><span>www.Velmo-LLC.com</span></div>
  </section>

  <section class="card front-light">
    <svg class="bg" width="351" height="200" viewBox="0 0 351 200">
      <path d="M0 0 H229 C205 42 160 66 82 66 H0 Z" fill="var(--red)"/>
      <circle cx="268" cy="57" r="46" fill="var(--red)" role="img" aria-label="Red dragon emblem illustration"/>
    </svg>
    <div class="holder-name">DANE ORWELL</div>
    <div class="holder-role">President</div>
    <div class="contact" style="left:22px;top:103px"><svg viewBox="0 0 10 10"><rect x="2.5" y=".5" width="5" height="9" rx="1" fill="none" stroke="var(--red)"/></svg><span><em>Office</em> 555-014-2290</span></div>
    <div class="contact" style="left:22px;top:126px"><svg viewBox="0 0 10 10"><rect x=".5" y="1.5" width="9" height="7" rx="1.5" fill="none" stroke="var(--red)"/><line x1="3.5" y1="1.5" x2="3.5" y2="8.5" stroke="var(--red)"/></svg><span><em>Cell</em> 555-018-3316</span></div>
    <div class="contact" style="left:22px;top:148px"><svg viewBox="0 0 10 10"><rect x=".5" y="2" width="9" height="6" fill="none" stroke="var(--red)"/><path d="M.5 2 L5 5.5 L9.5 2" fill="none" stroke="var(--red)"/></svg><span>DOrwell@velmo-llc.com</span></div>
    <div class="contact" style="left:197px;top:137px"><svg viewBox="0 0 10 10"><path d="M5 9.5 C2 6 1.5 4.5 1.5 3.5 a3.5 3.5 0 0 1 7 0 C8.5 4.5 8 6 5 9.5 Z" fill="none" stroke="var(--red)"/><circle cx="5" cy="3.6" r="1.2" fill="var(--red)"/></svg><span>1840 N. 200 East<br>Ashford, IN, 46000</span></div>
    <div class="contact web" style="left:197px;top:170px"><svg viewBox="0 0 10 10"><circle cx="5" cy="5" r="4.5" fill="none" stroke="var(--red)"/><ellipse cx="5" cy="5" rx="2" ry="4.5" fill="none" stroke="var(--red)"/><line x1=".5" y1="5" x2="9.5" y2="5" stroke="var(--red)"/></svg><span>www.Velmo-LLC.com</span></div>
  </section>

  <section class="card back-white">
    <div class="brand"><div class="brand-square"></div><div class="brand-name">VELMO</div></div>
  </section>

  <section class="card back-red">
    <div class="brand"><div class="brand-square"></div><div class="brand-name">VELMO</div></div>
  </section>

</div>
</body>
</html>
```